Australian Software Consultancy needs new Business Card Design

Design Business Card based on existing design artefacts (attached). We are open to all designs. As its a 2 sided design and we thought it might be quite striking to have one side with a black background and te other side with a white background.

Target Market(s)

Financial Services mainly.

Industry/Entity Type

Business

Contact Information for Business Card

Name :
Position :
Email :

Requirements
Must have
• Funky design using our existing assets

```html
<!DOCTYPE html>
<html lang="en">
<head>
<meta charset="utf-8">
<title>Northvale Labs Business Card</title>
<link rel="stylesheet" href="https://fonts.googleapis.com/css2?family=Montserrat:wght@700&family=Fira+Sans+Condensed:wght@400;600&family=Open+Sans:wght@400;700&display=swap">
<style>
  :root {
    --stage: #b3b3b3;
    --card-dark: #141414;
    --card-dark-glow: #3a3a3a;
    --card-light: #ffffff;
    --brand-red: #e61e25;
    --ink: #111111;
    --faint: #e6e6e6;
  }
  html, body {
    margin: 0;
    padding: 0;
    width: 1058px;
    height: 1200px;
    overflow: hidden;
    background: var(--stage);
  }
  .canvas {
    position: relative;
    width: 1058px;
    height: 1200px;
  }
  .card {
    position: absolute;
    left: 160px;
    width: 749px;
    height: 427px;
    overflow: hidden;
  }
  .card--front {
    top: 143px;
    background: radial-gradient(ellipse at 50% 40%, var(--card-dark-glow) 0%, var(--card-dark) 70%);
  }
  .card--back {
    top: 637px;
    left: 157px;
    background: var(--card-light);
  }
  .card__decor,
  .front-mark {
    position: absolute;
    left: 0;
    top: 0;
  }
  .front-mark__name {
    position: absolute;
    left: 0;
    width: 734px;
    top: 191px;
    text-align: center;
    font-family: "Montserrat", sans-serif;
    font-weight: 700;
    font-size: 20px;
    line-height: 26px;
    letter-spacing: 1px;
    color: var(--brand-red);
    white-space: nowrap;
  }
  .wordmark {
    position: absolute;
    left: 0;
    width: 749px;
    top: 58px;
    text-align: center;
    font-family: "Montserrat", sans-serif;
    font-weight: 700;
    font-size: 31px;
    line-height: 40px;
    letter-spacing: 1px;
    color: var(--ink);
    white-space: nowrap;
  }
  .person {
    position: absolute;
    left: 268px;
    top: 148px;
  }
  .person__name {
    font-family: "Fira Sans Condensed", sans-serif;
    font-size: 46px;
    line-height: 48px;
    color: var(--ink);
    white-space: nowrap;
  }
  .person__first { font-weight: 600; }
  .person__last { font-weight: 400; }
  .person__role {
    font-family: "Open Sans", sans-serif;
    font-weight: 700;
    font-size: 15px;
    line-height: 20px;
    letter-spacing: 1.6px;
    color: var(--brand-red);
    margin-top: -2px;
    white-space: nowrap;
  }
  .contact {
    position: absolute;
    left: 261px;
    top: 286px;
    font-family: "Open Sans", sans-serif;
    font-size: 18px;
    line-height: 24px;
    color: var(--ink);
    white-space: nowrap;
  }
</style>
</head>
<body>
<main class="canvas">
  <section class="card card--front" aria-label="Card front">
    <svg class="front-mark" width="749" height="427" viewBox="0 0 749 427" aria-hidden="true">
      <circle cx="367" cy="204" r="97" fill="none" stroke="var(--brand-red)" stroke-width="11"/>
    </svg>
    <div class="front-mark__name">NORTHVALE</div>
  </section>

  <section class="card card--back" aria-label="Card back">
    <svg class="card__decor" width="749" height="427" viewBox="0 0 749 427" aria-hidden="true">
      <circle cx="61" cy="212" r="163" fill="none" stroke="var(--faint)" stroke-width="22"/>
      <circle cx="703" cy="212" r="163" fill="none" stroke="var(--faint)" stroke-width="22"/>
    </svg>
    <div class="wordmark">NORTHVALE LABS</div>
    <div class="person">
      <div class="person__name"><span class="person__first">Marcus</span><span class="person__last">Lee</span></div>
      <div class="person__role">Founding Partner &amp; CEO</div>
    </div>
    <div class="contact">marcus@northvalelabs.com</div>
  </section>
</main>
</body>
</html>
```